Brenner & Holloway Stationery

Greetings again. Now we've got an awesome logo, it's time to get the stationery to go with it. We require the following items of stationery:

- Business Card - Print Ready, all we need to do is change names and numbers and submit to printer.  Double sided with logo on one side and details on the other side. (85mm x 55mm)

- With Compliments Slip

- Letterhead - These will be preprinted pages that will then be used as pages.
(A4)

- Envelope - Business Size(Standard DL)

Target Market(s)

Essentially, this firm services clients facing criminal charges and/or seeking legal aid. The firm is also looking at taking on more white-collar crime cases.

Requirements
Must have
• - Same Design Cues & Colours as the Branding details attached

• - Address (as follows)

• Suite 8

• 262-268 Marlow St

• KINGSBROOK VIC 3188

• Phone: (03) 9482 6315

• Fax: (03) 9482 6840

• Web: www.brennerandholloway.example.au

• - Colour: Pantone 194 (Red)

```html
<!DOCTYPE html>
<html lang="en">
<head>
<meta charset="utf-8">
<title>Brenner &amp; Holloway Stationery</title>
<link rel="stylesheet" href="https://fonts.googleapis.com/css2?family=Cinzel:wght@400;600&family=Open+Sans:wght@400&display=swap">
<style>
  :root {
    --backdrop: #6b6b6b;
    --brand-red: #a6093d;
    --paper: #ffffff;
    --ink: #2a2a2a;
    --soft-grey: #c9c9c9;
    --faint-grey: #9a9a9a;
    --shadow: #1c1c1c;
  }
  * { margin: 0; padding: 0; box-sizing: border-box; }
  html, body { width: 1200px; height: 883px; overflow: hidden; background: var(--backdrop); }
  .stage { position: relative; width: 1200px; height: 883px; background: var(--backdrop); overflow: hidden; }

  /* Letterhead */
  .letterhead { position: absolute; left: 241px; top: 22px; width: 568px; height: 845px; background: var(--paper); }
  .letterhead-frame { position: absolute; inset: 0; }
  .letterhead-brand { position: absolute; left: 129px; top: 728px; display: flex; align-items: center; gap: 14px; }
  .letterhead-brand .brand-dot { width: 58px; height: 58px; border-radius: 50%; background: #dcdcdc; }
  .letterhead-brand .brand-text { border-left: 1px solid #d6d6d6; padding-left: 12px; color: var(--soft-grey); font-family: "Cinzel", serif; }
  .letterhead-brand .brand-name { font-size: 22px; font-weight: 400; line-height: 1.1; }
  .letterhead-brand .brand-tag { font-size: 15px; line-height: 1.2; }
  .letterhead-footer { position: absolute; left: 18px; width: 492px; bottom: 8px; font-family: "Open Sans", sans-serif; font-size: 5px; color: var(--faint-grey); white-space: nowrap; overflow: hidden; text-align: center; }

  /* Business card */
  .business-card { position: absolute; left: 117px; top: 419px; width: 161px; height: 266px; background: var(--paper); overflow: hidden; }
  .card-watermark { position: absolute; left: 5px; top: 82px; width: 148px; height: 148px; border-radius: 50%; background: #e4e4e4; }
  .card-details { position: absolute; top: 14px; left: 4px; right: 4px; text-align: center; font-family: "Cinzel", serif; color: #8c8c8c; }
  .card-name { font-size: 11px; letter-spacing: 1px; color: #777; margin-bottom: 4px; }
  .card-line { font-size: 5.5px; line-height: 9px; letter-spacing: .3px; white-space: nowrap; }
  .card-line.email { font-size: 4.6px; letter-spacing: 0; }
  .card-brand { position: absolute; left: 6px; top: 206px; display: flex; align-items: center; gap: 5px; font-family: "Cinzel", serif; color: var(--ink); }
  .card-brand .brand-dot { width: 26px; height: 26px; border-radius: 50%; background: var(--brand-red); flex: none; }
  .card-brand .brand-text { border-left: 1px solid #bdbdbd; padding-left: 4px; }
  .card-brand .brand-name { font-size: 9.5px; font-weight: 600; line-height: 1.1; }
  .card-brand .brand-tag { font-size: 6.5px; font-weight: 600; }
  .card-web { position: absolute; left: 0; right: 0; bottom: 0; height: 14px; background: var(--brand-red); color: var(--paper); font-family: "Open Sans", sans-serif; font-size: 5.5px; line-height: 14px; padding-left: 6px; letter-spacing: .3px; white-space: nowrap; }

  /* Envelope */
  .envelope { position: absolute; left: 511px; top: 422px; width: 648px; height: 291px; background: var(--brand-red); padding: 13px; box-shadow: 14px 14px 0 var(--shadow); }
  .envelope-face { width: 100%; height: 100%; background: var(--paper); position: relative; }
  .envelope-brand { position: absolute; left: 13px; top: 4px; display: flex; align-items: center; gap: 7px; font-family: "Cinzel", serif; color: var(--ink); }
  .envelope-brand .brand-dot { width: 50px; height: 50px; border-radius: 50%; background: var(--brand-red); flex: none; }
  .envelope-brand .brand-text { border-left: 1px solid #bdbdbd; padding-left: 6px; }
  .envelope-brand .brand-name { font-size: 17px; font-weight: 600; line-height: 1.1; }
  .envelope-brand .brand-tag { font-size: 11px; font-weight: 600; }
</style>
</head>
<body>
<main class="stage">

  <section class="letterhead" aria-label="Letterhead">
    <svg class="letterhead-frame" width="568" height="845" viewBox="0 0 568 845" aria-hidden="true">
      <rect x="0" y="0" width="568" height="845" fill="var(--brand-red)"/>
      <path d="M0 122 Q140 40 292 24 L292 19 L522 19 L522 845 L0 845 Z" fill="var(--paper)"/>
      <g fill="var(--paper)">
        <rect x="518" y="44" width="50" height="4"/>
        <rect x="518" y="57" width="50" height="4"/>
        <rect x="518" y="70" width="50" height="4"/>
        <rect x="518" y="83" width="50" height="4"/>
      </g>
    </svg>
    <div class="letterhead-brand">
      <span class="brand-dot"></span>
      <div class="brand-text">
        <div class="brand-name">Brenner &amp; Holloway</div>
        <div class="brand-tag">Barristers &amp; Solicitors</div>
      </div>
    </div>
    <p class="letterhead-footer">Suite 8, 262-268 Marlow St | Kingsbrook VIC 3188 | P (03) 9482 6315 | F (03) 9482 6840 | info@brennerandholloway.example.au | www.brennerandholloway.example.au</p>
  </section>

  <section class="business-card" aria-label="Business card">
    <div class="card-watermark" aria-hidden="true"></div>
    <div class="card-details">
      <p class="card-name">Daniel Ashford</p>
      <p class="card-line">Suite 8, 262-268 Marlow St</p>
      <p class="card-line">Kingsbrook VIC 3188</p>
      <p class="card-line">P (03) 9482 6315</p>
      <p class="card-line">F (03) 9482 6840</p>
      <p class="card-line email">info@brennerandholloway.example.au</p>
    </div>
    <div class="card-brand">
      <span class="brand-dot"></span>
      <div class="brand-text">
        <div class="brand-name">Brenner &amp; Holloway</div>
        <div class="brand-tag">Barristers &amp; Solicitors</div>
      </div>
    </div>
    <p class="card-web">www.brennerandholloway.example.au</p>
  </section>

  <section class="envelope" aria-label="DL envelope">
    <div class="envelope-face">
      <div class="envelope-brand">
        <span class="brand-dot"></span>
        <div class="brand-text">
          <div class="brand-name">Brenner &amp; Holloway</div>
          <div class="brand-tag">Barristers &amp; Solicitors</div>
        </div>
      </div>
    </div>
  </section>

</main>
</body>
</html>
```